Radiant Crossroads - An Exciting Mission & Book Cover Project

Help me to inspire people to live their best life! This is a mission, not just a design project.
I need a Book Cover designed to keep me inspired on the process of writing my book.
Book Title: Radiant Crossroads
Tag Line: Three Simple Steps to get out of your own way, SuperCharge your Life and Step into Purpose!
Author: Marlon Teague

The three steps are: Ownership, Vision and Action (Not sure if this should be on the front or back of the book cover)

The book is a self-help, motivational book. Personal development.
The cover needs to be strong and capture peoples attention, especially with competing shelf space. I almost see a fire ball of flame or explosion that will grab peoples attention.
My company is The Summit Collective. I have added the company logo and a few pages of my presentation and topic outline to give an idea.
Maybe: The Summit Collective logo on back of the cover. website is marlonteague-example.com

THOUGHT: People should be able to take a photo of them holding the book cover showing what area of life they want Radiant Crossroads in. This is why the front cover must be so visual and powerful that they want to take a photo with it. Ie. Explosion, fire, strong and bold.

Target Market(s)

Anyone who feels stuck and needs to breakthrough and move forward in life.

Industry/Entity Type

Motivation

Font styles to use
Serif
Sans Serif

Colors
ec1f27
f37122
fbed22

Requirements
Must have
• The design must be STRONG, SIMPLE, STAND OUT ON BOOK SHELVES.
Must have an open file to swap the photo and copy out.

Back Cover Page
1) Summary
2) 2-3 testimonials. One sentence.
3) About the Author (maybe with photo)
4) Summit Collective logo
5) Website: radiantcrossroads-example.com and marlonteague-example.com
Nice to have
• If my photo works somewhere that would be great. I will change the photo later.
Added Where Does Your Compass Point? a nice cover example.
Should not have
• Right now I am writing the summary for the back of the cover. For now use Loreum Ipsum text and 2-3 recommendations. Again, I will get these only later.

```html
<!DOCTYPE html>
<html lang="en">
<head>
<meta charset="utf-8">
<title>Radiant Crossroads — Book Cover</title>
<link rel="stylesheet" href="https://fonts.googleapis.com/css2?family=Jost:wght@400;500;700&display=swap">
<style>
  :root {
    --bg-deep: #140403;
    --bg-mid: #3a0f07;
    --bg-glow: #7a2a0e;
    --title-yellow: #fbed22;
    --text-white: #ffffff;
    --flame-core: #fcd27a;
    --flame-mid: #f37122;
    --flame-edge: #ec1f27;
  }
  html, body {
    margin: 0;
    padding: 0;
    width: 800px;
    height: 1200px;
    overflow: hidden;
    background: var(--bg-deep);
  }
  .cover {
    position: relative;
    width: 800px;
    height: 1200px;
    overflow: hidden;
    font-family: "Jost", "Futura", sans-serif;
    background:
      radial-gradient(ellipse 520px 560px at 52% 74%, var(--bg-glow) 0%, var(--bg-mid) 45%, var(--bg-deep) 85%),
      var(--bg-deep);
  }
  .steps {
    position: absolute;
    top: 24px;
    left: 0;
    width: 800px;
    height: 40px;
    color: var(--text-white);
    font-size: 31px;
    font-weight: 400;
    letter-spacing: 0.5px;
  }
  .steps span { position: absolute; top: 0; line-height: 40px; }
  .steps .step-one { left: 73px; }
  .steps .step-two { left: 442px; transform: translateX(-50%); }
  .steps .step-three { right: 66px; }
  .steps .divider {
    position: absolute;
    top: 0;
    width: 1.5px;
    height: 40px;
    background: var(--text-white);
  }
  .steps .divider.first { left: 313px; }
  .steps .divider.second { left: 569px; }

  .title {
    position: absolute;
    left: 0;
    width: 800px;
    text-align: center;
    color: var(--title-yellow);
    margin: 0;
    font-weight: 400;
  }
  .title-main {
    top: 74px;
    font-size: 190px;
    line-height: 180px;
    letter-spacing: -2px;
  }
  .title-sub {
    top: 236px;
    font-size: 140px;
    line-height: 140px;
    letter-spacing: -1px;
  }

  .tagline-frame {
    position: absolute;
    left: 168px;
    top: 404px;
    width: 464px;
    height: 162px;
  }
  .tagline-frame svg { position: absolute; inset: 0; }
  .tagline {
    position: absolute;
    left: 0;
    right: 0;
    top: 14px;
    margin: 0;
    text-align: center;
    color: var(--text-white);
    font-size: 30px;
    line-height: 45px;
    font-weight: 400;
  }

  .hero-art {
    position: absolute;
    left: 100px;
    top: 566px;
    width: 660px;
    height: 520px;
    border-radius: 50%;
    background:
      radial-gradient(ellipse 40% 45% at 45% 45%, var(--flame-core) 0%, rgba(243,113,34,0.85) 45%, rgba(236,31,39,0.35) 75%, rgba(122,42,14,0) 100%);
    filter: blur(6px);
    opacity: 0.9;
  }
  .ground-glow {
    position: absolute;
    left: 250px;
    top: 1062px;
    width: 400px;
    height: 14px;
    border-radius: 50%;
    background: radial-gradient(ellipse at center, rgba(243,113,34,0.8) 0%, rgba(243,113,34,0) 70%);
  }

  .author {
    position: absolute;
    left: 0;
    top: 1106px;
    width: 800px;
    margin: 0;
    text-align: center;
    color: var(--text-white);
    font-size: 66px;
    line-height: 70px;
    letter-spacing: 0.5px;
  }
  .author .first-name { font-weight: 700; }
  .author .last-name { font-weight: 400; }
</style>
</head>
<body>
  <main class="cover">
    <div class="steps">
      <span class="step-one">OWNERSSHIP</span>
      <i class="divider first"></i>
      <span class="step-two">VISION</span>
      <i class="divider second"></i>
      <span class="step-three">ACTION</span>
    </div>

    <h1 class="title title-main">RADIANT</h1>
    <h2 class="title title-sub">Crossroads</h2>

    <div class="tagline-frame">
      <svg width="464" height="162" viewBox="0 0 464 162" fill="none" stroke="#ffffff" stroke-width="2">
        <polyline points="1,20 1,1 34,1"/>
        <polyline points="430,1 463,1 463,20"/>
        <polyline points="1,142 1,161 34,161"/>
        <polyline points="430,161 463,161 463,142"/>
      </svg>
      <p class="tagline">Three Simple Steps to get out<br>of your own way, SuperCharge<br>your Life and Step into Purpose!</p>
    </div>

    <div class="hero-art" role="img" aria-label="Illustration of a sprinting figure engulfed in orange flames"></div>
    <div class="ground-glow"></div>

    <p class="author"><span class="first-name">MARLON</span> <span class="last-name">TEAGUE</span></p>
  </main>
</body>
</html>
```